Business Card Design Project

Build kick ass business card.
Updates

I just uploaded the Veruxo Logo in AI format, for those that were asking. It's looking real good and we'll be reviewing the designs soon. Thanks. 

Target Market(s)

Businesses in many verticals. Focusing on information security.

Veruxo, LLC
Darren Colby
Principal Security Consultant
Mobile: +1-480-555-0137
Email: Darren.Colby@Veruxo.example
Web: www.veruxo.example

Industry/Entity Type

Business

Requirements
Must have
• Design must look high-end, hi-tech stylish and minimalist

Be different – one that stands out from thousands of others

Does not have to be traditional rectangle

Would like logo integrated

```html
<!DOCTYPE html>
<html lang="en">
<head>
<meta charset="utf-8">
<title>Veruxo Business Card</title>
<link rel="stylesheet" href="https://fonts.googleapis.com/css2?family=Source+Sans+3:wght@300;400;600;700&display=swap">
<style>
  :root {
    --backdrop: #8f1407;
    --card-white: #ffffff;
    --card-edge: #e4e4e4;
    --brand-blue: #2a93d5;
    --brand-blue-deep: #1d7fc4;
    --brand-blue-light: #45a9e4;
    --ink-dark: #2b2b2b;
    --ink-soft: #6f6f6f;
    --logo-grey: #3a3a3a;
  }
  * { box-sizing: border-box; margin: 0; padding: 0; }
  html, body {
    width: 1200px;
    height: 450px;
    overflow: hidden;
  }
  body {
    background: var(--backdrop);
    font-family: "Source Sans 3", "Helvetica Neue", Arial, sans-serif;
    display: flex;
    align-items: center;
    justify-content: center;
    gap: 80px;
  }
  .card {
    width: 490px;
    height: 280px;
    position: relative;
    overflow: hidden;
    box-shadow: 0 10px 28px rgba(0, 0, 0, 0.35);
  }

  /* Front */
  .card--front {
    background: radial-gradient(ellipse at center, var(--card-white) 62%, var(--card-edge) 100%);
    display: flex;
    flex-direction: column;
    align-items: center;
    justify-content: center;
  }
  .brand {
    display: flex;
    align-items: center;
    gap: 12px;
    margin-top: 8px;
  }
  .brand__dot {
    width: 34px;
    height: 34px;
    border-radius: 50%;
    background: var(--brand-blue);
  }
  .brand__name {
    font-size: 34px;
    font-weight: 400;
    letter-spacing: 2px;
    color: var(--logo-grey);
    text-transform: uppercase;
  }
  .front__url {
    margin-top: 34px;
    font-size: 15px;
    font-weight: 600;
    color: var(--brand-blue);
  }

  /* Back */
  .card--back {
    background: linear-gradient(180deg, #ffffff 0%, #f1f1f1 100%);
  }
  .back__band {
    position: absolute;
    left: 0; top: 0;
    width: 100%;
    height: 166px;
    background: linear-gradient(160deg, var(--brand-blue-deep) 0%, var(--brand-blue) 55%, var(--brand-blue-light) 100%);
    border-bottom: 3px solid #7ec4ee;
    text-align: center;
    padding-top: 60px;
    color: #fff;
  }
  .back__name {
    font-size: 24px;
    font-weight: 700;
    line-height: 1.1;
  }
  .back__title {
    font-size: 16px;
    font-weight: 400;
    margin-top: 2px;
  }
  .contact {
    position: absolute;
    top: 196px;
    left: 0;
    width: 100%;
    text-align: center;
    list-style: none;
    font-size: 13px;
    line-height: 1.3;
  }
  .contact__label { color: var(--ink-soft); }
  .contact__value { color: var(--ink-dark); font-weight: 600; }
</style>
</head>
<body>
  <section class="card card--front" aria-label="Card front">
    <div class="brand">
      <span class="brand__dot"></span>
      <span class="brand__name">Veruxo</span>
    </div>
    <p class="front__url">www.veruxo.example</p>
  </section>

  <section class="card card--back" aria-label="Card back">
    <header class="back__band">
      <h1 class="back__name">Darren Colby</h1>
      <p class="back__title">Principal Security Consultant</p>
    </header>
    <ul class="contact">
      <li><span class="contact__label">Mobile.</span> <span class="contact__value">+1-480-555-0137</span></li>
      <li><span class="contact__label">Email.</span> <span class="contact__value">Darren.Colby@Veruxo.example</span></li>
      <li><span class="contact__label">Website.</span> <span class="contact__value">www.veruxo.example</span></li>
    </ul>
  </section>
</body>
</html>
```